Korvix App Graphics Design

Our application promotes location based self expression via pictures and text. The primary focus of the application is on the content posted and not on the person that posted it.

We want a very clean and fresh design that evokes positive energy. Our site is unique so our design should be as well. People will reveal thoughts on our site, so the design should convey a "revealing" feel. Our site is a place where people are comfortable to freely express themselves. Colors we have in mind are blue and green hues with earth tones for background.

Our project is to design ten screens for our Korvix application at resolution of 1136-by-640 pixels:

Feed Screen
Camera Screen
Post Screen
Check In Screen
Approval Screen
Map Screen
Flag Screen
Feed Select Screen
Export Screen
Menu Screen

In the contest phase we will require only three screens to be submitted. The screens we require to be submitted are: Feed Screen; Map Screen and Camera Screen. The designer we select as the winner of the competition will then complete the project and deliver a total of the ten screens described above in the handover phase.

We have attached a document below with detailed specs of each screen, we ask for your innovation to bring these screens to life through your design.
Updates

We want to clarify one aspect regarding the VISOR: the visor needs to be transparent so that when the picture scrolls underneath it, you can still see the picture underneath the visor.

Hi Everyone,

We have noticed that some designers need clarification regarding the visor element in the feed screen.
I have attached two examples to our brief area called:
Visor Example 1 and Visor Example 2

Please note that these are not the style we are looking for but are a good example to the concept of a Transparent Visor above the feed stream. We are looking for you guys to come up with a Visor concept that is consistent with the style of the design you are submitting.

Thanks,

Bo

Target Market(s)

People 17-40 who want to share their thought about the world around them.

Industry/Entity Type

Flag

Font styles to use
Sans Serif
Other font styles liked:
• We like “Helvetica New” or “Avenir” but are flexible

Requirements
Must have
• Visor component should look innovative.

```html
<!DOCTYPE html>
<html lang="en">
<head>
<meta charset="utf-8">
<title>Korvix App Screens</title>
<link rel="stylesheet" href="https://fonts.googleapis.com/css2?family=Arimo:wght@400;700&display=swap">
<style>
:root{
  --stage:#000;
  --status:#1a1a1a;
  --toolbar:#262626;
  --btn-top:#3fb3ea;
  --btn-bot:#1582c6;
  --btn-line:#0d6aa5;
  --visor-a:#23285c;
  --visor-b:#3c4590;
  --navy:#36346a;
  --navy-line:#55538a;
  --panel:#c9cacd;
  --panel-light:#d9dadc;
  --ink:#1c1c1c;
  --white:#fff;
  --map:#ebe7df;
  --map-road:#f7f6f2;
  --green:#5cb85c;
  --pin-red:#d8453a;
}
*{box-sizing:border-box;margin:0;padding:0}
html,body{width:1200px;height:772px;overflow:hidden;background:var(--stage);font-family:"Arimo",Helvetica,Arial,sans-serif}
.canvas{position:relative;width:1200px;height:772px;background:var(--stage)}
.screen{position:absolute;top:197px;width:246px;background:var(--panel);overflow:hidden}
.screen--feed{left:184px;height:370px}
.screen--camera{left:479px;height:370px;background:var(--toolbar)}
.screen--map{left:773px;height:354px;background:var(--map)}
.statusbar{position:absolute;left:0;top:0;width:100%;height:16px;background:var(--status);color:#e8e8e8;font-size:10px;font-weight:700;display:flex;align-items:center;padding:0 5px}
.statusbar .carrier{flex:1;display:flex;align-items:center;gap:4px}
.statusbar .time{position:absolute;left:50%;transform:translateX(-50%)}
.statusbar .right{display:flex;align-items:center;gap:4px}
.bars{display:flex;align-items:flex-end;gap:1px}
.bars i{display:block;width:2px;background:#ddd}
.battery{width:17px;height:8px;border:1px solid #ddd;padding:1px}
.battery b{display:block;width:100%;height:100%;background:#ddd}
.toolbar{position:absolute;left:0;top:16px;width:100%;height:32px;background:var(--toolbar);display:flex;align-items:center;justify-content:space-between;padding:0 12px}
.screen--camera .toolbar{padding:0 3px}
.btn{height:16px;border-radius:4px;background:linear-gradient(var(--btn-top),var(--btn-bot));border:1px solid var(--btn-line);color:var(--white);font-size:8px;display:flex;align-items:center;justify-content:center;gap:3px;box-shadow:inset 0 1px 0 rgba(255,255,255,.35)}
.toolbar .btn{width:59px}
.screen--camera .toolbar .btn{width:57px}
.visor{position:absolute;left:0;top:48px;width:100%;height:45px;background:linear-gradient(90deg,var(--visor-a),var(--visor-b) 50%,var(--visor-a))}
.photo{position:absolute;left:0;width:100%}
.photo--mall{top:93px;height:126px;background:linear-gradient(#e8ecef 0%,#c7ccd0 40%,#8c8f8c 75%,#5f6a52 100%)}
.photo--shop{top:93px;height:180px;background:linear-gradient(#2a1a12,#7a4a2a 45%,#c79b6e 70%,#e6d8c8)}
.chip{position:absolute;top:96px;height:15px;border-radius:3px;background:#3b3f58;border:1px solid #6b7090;color:var(--white);font-size:8px;display:flex;align-items:center;gap:3px;padding:0 8px}
.chip--flag{left:8px;width:58px}
.chip--export{right:8px;width:58px}
.stats{position:absolute;left:0;top:219px;width:100%;height:22px;background:var(--panel-light);display:flex;font-size:8px;color:#333}
.stats span{display:flex;align-items:center;justify-content:center;gap:3px;border-right:1px solid #aaa}
.stats span:last-child{border:0}
.votes{position:absolute;left:0;top:241px;width:100%;height:32px;background:var(--navy);display:flex}
.votes span{flex:1;display:flex;align-items:center;justify-content:center;gap:5px;color:var(--white);font-size:8px}
.votes span+span{border-left:1px solid var(--navy-line)}
.place{position:absolute;left:18px;top:282px;color:var(--ink);font-size:7px;line-height:10px}
.place strong{font-size:7.5px}
.next{position:absolute;left:36px;top:310px;width:173px;height:22px;border-radius:6px;background:linear-gradient(#5a5890,#2f2d62);border:1px solid #1c1a40;color:var(--white);font-size:10px;display:flex;align-items:center;justify-content:center;gap:8px}
.bottombar{position:absolute;left:0;bottom:0;width:100%;height:32px;background:var(--toolbar);display:flex;align-items:center;justify-content:space-between;padding:0 12px}
.bottombar .btn{width:59px}
.filters{position:absolute;left:0;top:273px;width:100%;height:58px;background:#9a9a9c;display:flex;gap:4px;padding:4px 3px}
.filter{flex:1;display:flex;flex-direction:column}
.filter .thumb{flex:1;background:linear-gradient(#3a2418,#a46c46 60%,#dcc6b0)}
.filter:nth-child(2) .thumb{background:linear-gradient(#4a2030,#c07a8a 60%,#f0d0d8)}
.filter:nth-child(3) .thumb{background:linear-gradient(#2a2a24,#b09a60 60%,#e8dcc0)}
.filter:nth-child(4) .thumb{background:linear-gradient(#40181c,#c46a70 60%,#f2d2d0)}
.filter span{height:11px;background:#2b2b2b;color:var(--white);font-size:8px;text-align:center;line-height:11px}
.camerabar{position:absolute;left:0;top:343px;width:100%;display:flex;justify-content:space-between;padding:0 2px}
.camerabar .btn{width:46px;height:13px;font-size:6px}
.placelist{position:absolute;left:0;top:16px;width:100%}
.placelist .gap{height:15px;background:#d6d6d6}
.placelist li{list-style:none;height:23px;background:var(--navy);border-top:1px solid var(--navy-line);color:var(--white);font-size:7px;display:flex;align-items:center;gap:13px;padding-left:8px}
.mapview{position:absolute;left:0;top:100px;width:100%;height:254px;background:linear-gradient(135deg,var(--map),#e2ded4 60%,#d9e3d3)}
.zoom{position:absolute;left:8px;top:110px;width:20px;height:20px;border-radius:50%;background:#f4f4f4;border:1px solid #aaa}
.zoombar{position:absolute;left:14px;top:140px;width:8px;height:118px;background:#f4f4f4;border:1px solid #aaa}
.zoombar::before{content:"";position:absolute;left:1px;top:10px;width:4px;height:16px;background:#e8a33a;border-radius:2px}
.lens{position:absolute;left:61px;top:138px;width:132px;height:132px;border-radius:50%;border:3px solid #2a2a2a}
.lens-knob{position:absolute;left:76px;top:144px;width:28px;height:28px;border-radius:50%;background:#333}
.eta{position:absolute;left:29px;top:182px;width:46px;height:36px;background:var(--green);color:var(--white);font-size:8px;display:flex;flex-direction:column;align-items:center;justify-content:center;gap:3px;border-radius:2px}
.callout{position:absolute;left:73px;top:182px;width:154px;height:38px;background:rgba(250,250,250,.94);border:1px solid #bbb;padding:4px 4px}
.callout b{display:block;font-size:11px;color:var(--ink)}
.callout span{display:block;font-size:7px;color:#333;margin-top:3px;white-space:nowrap;overflow:hidden}
.redpin{position:absolute;left:206px;top:221px}
.mapactions{position:absolute;left:55px;top:330px;display:flex;gap:5px}
.mapactions .btn{width:59px;height:16px;font-size:6px}
</style>
</head>
<body>
<div class="canvas">

  <!-- Feed screen -->
  <section class="screen screen--feed">
    <div class="statusbar">
      <span class="carrier"><span class="bars"><i style="height:3px"></i><i style="height:4px"></i><i style="height:5px"></i><i style="height:6px"></i><i style="height:7px"></i></span>Telvano NL</span>
      <span class="time">08:39</span>
      <span class="right">100% <span class="battery"><b></b></span></span>
    </div>
    <div class="toolbar">
      <span class="btn">&#8942; Menu</span>
      <span class="btn">&#9676; Feed</span>
      <span class="btn">&#9906; Search</span>
    </div>
    <div class="visor" role="img" aria-label="Transparent visor with a dotted world map pattern"></div>
    <div class="photo photo--mall" role="img" aria-label="Photo of a shopping mall building"></div>
    <span class="chip chip--flag"><svg width="8" height="8" viewBox="0 0 8 8"><path d="M1 0v8M1 1h6l-2 2 2 2H1" fill="#fff" stroke="#fff" stroke-width=".8"/></svg> Flag</span>
    <span class="chip chip--export"><svg width="8" height="8" viewBox="0 0 8 8"><rect x=".5" y="2.5" width="5" height="5" fill="none" stroke="#fff"/><path d="M3 5l4-4M5 1h2v2" stroke="#fff" fill="none"/></svg> Export</span>
    <div class="stats">
      <span style="width:77px">&#8260; 26 Mi</span>
      <span style="width:92px">5 Post</span>
      <span style="width:77px">&#9201; 30 min</span>
    </div>
    <div class="votes">
      <span><svg width="10" height="10" viewBox="0 0 10 10"><circle cx="5" cy="5" r="5" fill="#fff"/><path d="M3 7V4h1l1-2v2h2l-1 3z" fill="#36346a"/></svg> PROMOTE</span>
      <span><svg width="10" height="10" viewBox="0 0 10 10"><circle cx="5" cy="5" r="5" fill="#fff"/><path d="M3 3l4 4M7 3l-4 4" stroke="#36346a" stroke-width="1.4"/></svg> DEMOTE</span>
    </div>
    <p class="place"><strong>Plaza Meridia</strong><br>Jl. Kenari Raya Kav. 12 - 14, Sawah Besar, Kota Selatan, Indonesia</p>
    <span class="next"><svg width="11" height="11" viewBox="0 0 11 11"><circle cx="5.5" cy="5.5" r="5.5" fill="#1c1a40"/><path d="M4 3l3 2.5L4 8" stroke="#fff" stroke-width="1.4" fill="none"/></svg> Next Picture</span>
    <div class="bottombar">
      <span class="btn"><svg width="10" height="8" viewBox="0 0 10 8"><rect x=".5" y="1.5" width="9" height="6" rx="1" fill="#fff"/><circle cx="5" cy="4.5" r="1.8" fill="#1582c6"/></svg></span>
      <span class="btn"><svg width="10" height="10" viewBox="0 0 10 10"><circle cx="5" cy="5" r="5" fill="#fff"/><path d="M2.8 5.2l1.6 1.6L7.4 3.6" stroke="#1582c6" stroke-width="1.4" fill="none"/></svg></span>
    </div>
  </section>

  <!-- Camera screen -->
  <section class="screen screen--camera">
    <div class="statusbar">
      <span class="carrier"><span class="bars"><i style="height:3px"></i><i style="height:4px"></i><i style="height:5px"></i><i style="height:6px"></i><i style="height:7px"></i></span>Telvano NL</span>
      <span class="time">08:39</span>
      <span class="right">100% <span class="battery"><b></b></span></span>
    </div>
    <div class="toolbar">
      <span class="btn">&#9889; Flash</span>
      <span class="btn">&#8635; Rotate</span>
      <span class="btn">&#9678; Focus</span>
      <span class="btn">Cancel</span>
    </div>
    <div class="visor" role="img" aria-label="Transparent visor with a dotted world map pattern"></div>
    <div class="photo photo--shop" role="img" aria-label="Photo of a bakery shop counter with display cases"></div>
    <div class="filters">
      <div class="filter"><div class="thumb" role="img" aria-label="Vivid filter preview"></div><span>Vivid</span></div>
      <div class="filter"><div class="thumb" role="img" aria-label="Ansel filter preview"></div><span>Ansel</span></div>
      <div class="filter"><div class="thumb" role="img" aria-label="Instant filter preview"></div><span>Instant</span></div>
      <div class="filter"><div class="thumb" role="img" aria-label="Pro filter preview"></div><span>Pro</span></div>
    </div>
    <div class="camerabar">
      <span class="btn">&#8635; Retake</span>
      <span class="btn">&#9728; Brightness</span>
      <span class="btn">&#9673; Take Photo</span>
      <span class="btn">&#8982; Crop</span>
      <span class="btn">&#10038; Effect</span>
    </div>
  </section>

  <!-- Map screen -->
  <section class="screen screen--map">
    <div class="statusbar">
      <span class="carrier"><span class="bars"><i style="height:3px"></i><i style="height:4px"></i><i style="height:5px"></i><i style="height:6px"></i><i style="height:7px"></i></span>Telvano NL</span>
      <span class="time">08:39</span>
      <span class="right">100% <span class="battery"><b></b></span></span>
    </div>
    <ul class="placelist">
      <li class="gap"></li>
      <li><svg width="11" height="11" viewBox="0 0 11 11"><path d="M6 0l5 5-2 0-3 3 0 2-5-5 2 0 3-3zM3 8l-3 3" fill="#fff" stroke="#fff"/></svg>Hotel Larasati</li>
      <li><svg width="11" height="11" viewBox="0 0 11 11"><path d="M6 0l5 5-2 0-3 3 0 2-5-5 2 0 3-3zM3 8l-3 3" fill="#fff" stroke="#fff"/></svg>Cendana City</li>
      <li><svg width="11" height="11" viewBox="0 0 11 11"><path d="M6 0l5 5-2 0-3 3 0 2-5-5 2 0 3-3zM3 8l-3 3" fill="#fff" stroke="#fff"/></svg>Gelora Satria Stadium</li>
    </ul>
    <div class="mapview" role="img" aria-label="Street map of the city centre around the dropped pin"></div>
    <span class="zoom"></span>
    <span class="zoombar"></span>
    <span class="lens"></span>
    <span class="lens-knob"></span>
    <div class="eta"><svg width="16" height="9" viewBox="0 0 16 9"><path d="M2 4l2-3h8l2 3h1v4H1V4z" fill="#fff"/></svg>35 min</div>
    <div class="callout"><b>Dropped Pin</b><span>Jl. Kenari Raya Kav. 12 - 14, Sawah.....</span></div>
    <svg class="redpin" width="9" height="13" viewBox="0 0 9 13"><path d="M4.5 13L1 6a4 4 0 1 1 7 0z" fill="var(--pin-red)"/><circle cx="4.5" cy="4.5" r="1.5" fill="#fff"/></svg>
    <div class="mapactions">
      <span class="btn"><svg width="8" height="8" viewBox="0 0 8 8"><circle cx="4" cy="4" r="4" fill="#fff"/><path d="M2 4l1.4 1.4L6 2.6" stroke="#1582c6" fill="none"/></svg> Done</span>
      <span class="btn">Current Location</span>
    </div>
  </section>

</div>
</body>
</html>
```